Quarry Vale Business Cards

We need to design some upbeat business cards. We are an Industrial Rope Access Company/Height Safety Company that specialize in Rope Access, Confined Space, Anchor Points, Safety Systems, PPE Inspecions and Rigging.
Company name is Quarry Vale Ltd
Card is for Reggie Stanton the Company Director
His mobile number is 027 816 4920 and email is reggie@quarryvale.co.nz. Website address is www.quarryvale.co.nz.
We will post some pictures below to ensure you get a good idea of what we do.

```html
<!DOCTYPE html>
<html lang="en">
<head>
<meta charset="utf-8">
<title>Quarry Vale Business Cards</title>
<link rel="stylesheet" href="https://fonts.googleapis.com/css2?family=Orbitron:wght@800&family=Exo+2:wght@400;700&display=swap">
<style>
  :root {
    --navy: #232659;
    --blue: #3757d6;
    --white: #ffffff;
    --ink: #1e2150;
    --grey-text: #4a4d6a;
    --backdrop-light: #8a9590;
    --backdrop-dark: #3f4644;
  }
  * { margin: 0; padding: 0; box-sizing: border-box; }
  html, body { width: 1200px; height: 900px; overflow: hidden; }
  body {
    background: radial-gradient(ellipse at 45% 40%, var(--backdrop-light), var(--backdrop-dark));
    font-family: "Exo 2", sans-serif;
    position: relative;
  }
  .card {
    position: absolute;
    width: 600px;
    height: 343px;
    left: 300px;
    border-radius: 24px;
    overflow: hidden;
    background: var(--white);
    box-shadow: 0 10px 30px rgba(0,0,0,.35);
  }
  .card--contact { top: 72px; }
  .card--services { top: 485px; }

  /* contact side */
  .contact-panel {
    position: absolute; left: 0; top: 0; bottom: 0; width: 190px;
    background: var(--navy); overflow: hidden;
  }
  .contact-panel__type {
    position: absolute; right: -40px; top: -28px;
    font-family: "Orbitron", sans-serif; font-weight: 800;
    font-size: 210px; line-height: .9; color: var(--blue);
    text-align: right; white-space: nowrap;
  }
  .wordmark {
    position: absolute; left: 208px; top: 150px;
    font-family: "Orbitron", sans-serif; font-weight: 800;
    font-size: 24px; color: var(--ink); white-space: nowrap;
  }
  .contact-divider {
    position: absolute; left: 420px; top: 120px; width: 1.5px; height: 110px;
    background: var(--ink);
  }
  .contact-details { position: absolute; left: 432px; top: 118px; color: var(--grey-text); font-size: 12.5px; }
  .contact-details__name { font-weight: 700; color: var(--ink); font-size: 15px; }
  .contact-details__role { margin-bottom: 6px; }
  .contact-details__row { display: flex; align-items: center; gap: 7px; margin-top: 5px; }
  .contact-details__icon { width: 15px; height: 15px; flex: none; }

  /* services side */
  .services-list {
    position: absolute; left: 0; top: 0; bottom: 0; width: 160px;
    padding: 62px 14px 0 0; list-style: none; text-align: right;
    font-size: 11px; letter-spacing: 2.6px; line-height: 17px; color: var(--grey-text);
    text-transform: uppercase;
  }
  .services-panel {
    position: absolute; left: 160px; top: 0; right: 0; bottom: 0;
    background: var(--navy); overflow: hidden;
  }
  .services-panel__type {
    position: absolute; left: 12px; top: -40px;
    font-family: "Orbitron", sans-serif; font-weight: 800;
    font-size: 190px; line-height: 1; color: var(--blue); white-space: nowrap;
  }
</style>
</head>
<body>
  <section class="card card--contact" aria-label="Business card, contact side">
    <div class="contact-panel" aria-hidden="true">
      <div class="contact-panel__type">ry<br>le</div>
    </div>
    <div class="wordmark">Quarry Vale</div>
    <div class="contact-divider"></div>
    <div class="contact-details">
      <div class="contact-details__name">Reggie Stanton</div>
      <div class="contact-details__role">Quarry Vale Ltd / Director</div>
      <div class="contact-details__row">
        <svg class="contact-details__icon" viewBox="0 0 16 16"><circle cx="8" cy="8" r="8" fill="var(--ink)"/><path d="M5.5 4.5h1.6l.7 2-1 .8a5 5 0 0 0 2 2l.8-1 2 .7v1.6c-3.5.4-6.5-2.6-6.1-6.1z" fill="#fff"/></svg>
        <span>(027) 816 4920</span>
      </div>
      <div class="contact-details__row">
        <svg class="contact-details__icon" viewBox="0 0 16 16"><circle cx="8" cy="8" r="8" fill="var(--ink)"/><rect x="4" y="5.2" width="8" height="5.6" fill="#fff"/><path d="M4 5.2l4 3 4-3" stroke="var(--ink)" fill="none" stroke-width=".9"/></svg>
        <span>reggie@quarryvale.co.nz</span>
      </div>
      <div class="contact-details__row">
        <svg class="contact-details__icon" viewBox="0 0 16 16"><circle cx="8" cy="8" r="8" fill="var(--ink)"/><g stroke="#fff" fill="none" stroke-width=".9"><circle cx="8" cy="8" r="4.5"/><ellipse cx="8" cy="8" rx="2" ry="4.5"/><path d="M3.5 8h9"/></g></svg>
        <span>www.quarryvale.co.nz</span>
      </div>
    </div>
  </section>

  <section class="card card--services" aria-label="Business card, services side">
    <ul class="services-list">
      <li>Rope Access</li>
      <li>Anchor Points</li>
      <li>PPE Certification</li>
      <li>Confined Space</li>
      <li>Safety Systems</li>
      <li>Rigging</li>
    </ul>
    <div class="services-panel" aria-hidden="true">
      <div class="services-panel__type">Quarry<br>Vale</div>
    </div>
  </section>
</body>
</html>
```